Halvorsen Basin Holdings, LP Letter Head

We need an official company letter head design that is clean and mimics our company logo style. It will include our logo, address, phone, and website. We are an OIl and Gas mineral purchasing company, so hints of oil rigs or related design would be desirable.

Industry/Entity Type

Oil And Gas

Colors
ec1f27
f04a50
f59195
fbd4d5

Requirements
Must have
• Logo
• 7316 Marwick T. Ellsbury Parkway, Suite 418
• Dallas TX, 75391
• 214-763-1957
• www.halvorsenbasin.com
Nice to have
• Oil Rigs or OIl and gas related design

```html
<!DOCTYPE html>
<html lang="en">
<head>
<meta charset="utf-8">
<title>Halvorsen Basin Holdings, LP – Letterhead</title>
<link href="https://fonts.googleapis.com/css2?family=PT+Sans:wght@400;700&display=swap" rel="stylesheet">
<style>
  :root {
    --brand-red: #c8141c;
    --ink: #2a2a2a;
    --ink-soft: #3c3c3c;
    --rule-dark: #3d3d3d;
    --paper: #f6f6f6;
    --backdrop: #e2e3e3;
    --signature-tone: #d9d9d9;
  }
  * { margin: 0; padding: 0; box-sizing: border-box; }
  html, body {
    width: 1200px; height: 945px; overflow: hidden;
    background: var(--backdrop);
    font-family: "PT Sans", sans-serif;
  }
  .letterhead {
    position: absolute; left: 250px; top: 20px;
    width: 700px; height: 905px;
    background: var(--paper);
    box-shadow: 0 2px 10px rgba(0,0,0,0.12);
  }
  .brand {
    position: absolute; left: 62px; top: 52px;
    display: flex; align-items: center; gap: 10px;
  }
  .brand-mark { width: 34px; height: 34px; background: var(--brand-red); }
  .brand-name {
    color: var(--brand-red);
    font-size: 21px; font-weight: 700; line-height: 1.05;
    width: 190px;
  }
  .letter-body {
    position: absolute; left: 80px; top: 205px; width: 540px;
    color: var(--ink-soft); font-size: 13.5px; line-height: 18px;
  }
  .salutation {
    font-family: Arial, "PT Sans", sans-serif;
    font-weight: 700; font-size: 15px; color: var(--ink);
    margin-bottom: 12px;
  }
  .letter-body p { margin-bottom: 18px; }
  .signature {
    position: absolute; left: 92px; top: 535px;
    width: 165px; height: 60px;
    background: var(--signature-tone); border-radius: 4px;
  }
  .footer-band { position: absolute; left: 0; bottom: 0; width: 700px; height: 80px; }
  .footer-contact {
    position: absolute; left: 80px; bottom: 26px;
    display: flex; align-items: center; gap: 12px;
    font-size: 11px; line-height: 14px; color: var(--ink-soft);
    white-space: nowrap;
  }
  .footer-contact span { display: flex; align-items: center; gap: 4px; }
  .footer-web {
    position: absolute; right: 28px; bottom: 20px;
    font-size: 11px; line-height: 14px; color: #fff; letter-spacing: 0.3px;
  }
</style>
</head>
<body>
  <main class="letterhead">
    <header class="brand">
      <div class="brand-mark"></div>
      <div class="brand-name">Halvorsen Basin Holdings</div>
    </header>

    <section class="letter-body">
      <div class="salutation">Dear Mr. Adler,</div>
      <p>Lorem Ipsum is simply dummy text of the printing and typesetting industry. Lorem Ipsum has been the industry's standard dummy text ever since the 1500s, when an unknown printer took a galley of type and scrambled it to make a type specimen book. It has survived not only five centuries, but also the leap into electronic typesetting, remaining essentially unchanged.</p>
      <p>The standard chunk of Lorem Ipsum used since the 1500s is reproduced below for those interested. Sections 1.10.32 and 1.10.33 from "de Finibus Bonorum et Malorum" by Varrenus are also reproduced in their exact original form, accompanied by English versions from the 1914 translation by H. Ellworth</p>
      <p>Lorem Ipsum is simply dummy text of the printing and typesetting industry. Lorem Ipsum has been the industry's standard dummy text ever since the 1500s, when an unknown printer took a galley of type and scrambled it to make a type specimen book. It has survived not only five centuries, but also the leap into electronic typesetting, remaining essentially unchanged. It was popularised in the</p>
    </section>

    <div class="signature" role="img" aria-label="Handwritten signature of the sender"></div>

    <svg class="footer-band" viewBox="0 0 700 80" aria-hidden="true">
      <path d="M0 58 L520 58 C540 58 542 40 566 40 L700 40 L700 44 L570 44 C546 44 544 62 524 62 L0 62 Z" fill="var(--rule-dark)"/>
      <path d="M0 62 L524 62 C544 62 546 44 570 44 L700 44 L700 80 L0 80 Z" fill="var(--brand-red)"/>
    </svg>

    <div class="footer-contact">
      <span>
        <svg width="11" height="11" viewBox="0 0 24 24" aria-hidden="true"><path fill="var(--brand-red)" d="M6.6 10.8a15.1 15.1 0 0 0 6.6 6.6l2.2-2.2c.3-.3.7-.4 1-.2 1.1.4 2.3.6 3.6.6.6 0 1 .4 1 1V20c0 .6-.4 1-1 1A17 17 0 0 1 3 4c0-.6.4-1 1-1h3.5c.6 0 1 .4 1 1 0 1.3.2 2.5.6 3.6.1.3 0 .7-.2 1z"/></svg>
        214-763-1957
      </span>
      <span>
        <svg width="10" height="12" viewBox="0 0 20 24" aria-hidden="true"><path fill="var(--brand-red)" d="M10 0a8 8 0 0 0-8 8c0 6 8 16 8 16s8-10 8-16a8 8 0 0 0-8-8zm0 11a3 3 0 1 1 0-6 3 3 0 0 1 0 6z"/></svg>
        7316 Marwick T. Ellsbury Parkway, Suite 418 Dallas TX, 75391
      </span>
    </div>
    <div class="footer-web">www.halvorsenbasin.com</div>
  </main>
</body>
</html>
```